Book a car wash

The app will have a logo, contact details and address
It will then lead you to booking a service from list
The customer will have a date, day and time

Booking - There are two types of times arrival is the main - day, date, time, service, payment. Each car takes and average of 1.5 hours

Pay by qlink or fundly or merchant

List of services
Bronze $25
Silver $40
Gold $55
Leather Plus $90
Diamond $100
Ruby $100
Standard Vehicle $0
Larger Vehicle & 4wd $10

Target Market(s)

Professionals with time issues
Parents with time management concerns

Industry/Entity Type

It Service

Requirements
Must have
• Logo
Menu list
Payment system
Address and contact details
Basement CarPark - Wexley Court Shopping Centre
Tarvin rd, Claremont
0493520741
Nice to have
• Big fonts and step by step process
Should not have
• No cars or washing items i.e. sponges

```html
<!DOCTYPE html>
<html lang="en">
<head>
<meta charset="utf-8">
<title>Book a Car Wash – Sign In and Payment Screens</title>
<link rel="stylesheet" href="https://fonts.googleapis.com/css2?family=Nunito:wght@300;400&display=swap">
<style>
  :root {
    --brand-orange: #fbb040;
    --field-line: #f7b640;
    --field-line-soft: #f6c46a;
    --text-heading: #8a8a8a;
    --text-label: #a3a3a3;
    --text-label-light: #c2c2c2;
    --keyboard-grey: #b3b3b3;
    --screen-edge: #e2e2e2;
    --screen-edge-active: #fff23a;
    --canvas-bg: #ffffff;
    --white: #ffffff;
  }
  * { box-sizing: border-box; margin: 0; padding: 0; }
  html, body {
    width: 1200px; height: 675px; overflow: hidden;
    background: var(--canvas-bg);
    font-family: "Nunito", sans-serif;
  }
  .canvas { position: relative; width: 1200px; height: 675px; }

  .screen {
    position: absolute;
    width: 328px; height: 499px;
    background: linear-gradient(to bottom, #ffffff 55%, #f1f1f1 100%);
    overflow: hidden;
  }
  .screen--sign-in {
    left: 225px; top: 68px;
    border-right: 1px solid var(--screen-edge);
    border-left: 1px solid var(--screen-edge);
  }
  .screen--payment {
    left: 623px; top: 71px;
    border: 1px solid var(--screen-edge-active);
  }

  .app-bar {
    position: absolute; left: 0; top: 0; right: 0; height: 55px;
    background: var(--brand-orange);
  }
  .app-bar__title {
    position: absolute; left: 0; right: 0; top: 0; height: 55px;
    line-height: 55px; text-align: center;
    color: var(--white); font-weight: 300; font-size: 21px;
  }
  .app-bar__icon { position: absolute; top: 10px; width: 36px; height: 36px; }
  .app-bar__icon--back { left: 10px; }
  .app-bar__icon--settings { right: 10px; }

  .screen__heading {
    position: absolute; left: 0; right: 0; top: 92px;
    text-align: center; color: var(--text-heading);
    font-weight: 300; font-size: 18.5px;
  }

  .field {
    position: absolute; left: 39px; width: 248px; height: 20px;
    border-bottom: 1px solid var(--field-line);
    padding-left: 10px;
    font-weight: 300; font-size: 13px; line-height: 18px;
    color: var(--text-label-light);
  }
  .screen--payment .field {
    border-bottom-color: var(--field-line-soft);
    color: var(--text-label);
  }

  .action-button {
    position: absolute; left: 47px; width: 231px; height: 41px;
    border: 1px solid var(--brand-orange);
    color: var(--brand-orange);
    text-align: center; line-height: 39px;
    font-weight: 300; font-size: 18px;
    background: transparent;
  }

  .keyboard {
    position: absolute; left: 0; right: 0; top: 350px; bottom: 0;
    background: var(--keyboard-grey);
    color: var(--white); text-align: center;
    font-weight: 300; font-size: 18px; padding-top: 18px;
  }
</style>
</head>
<body>
<div class="canvas">

  <section class="screen screen--sign-in" aria-label="Sign in screen">
    <header class="app-bar">
      <svg class="app-bar__icon app-bar__icon--back" viewBox="0 0 36 36" aria-label="Back">
        <circle cx="18" cy="18" r="16" fill="none" stroke="#fff" stroke-width="2.5"/>
        <circle cx="18" cy="18" r="10" fill="#fff"/>
        <path d="M23 18H13M17.5 13.5L13 18l4.5 4.5" fill="none" stroke="#fbb040" stroke-width="2.6" stroke-linecap="round" stroke-linejoin="round"/>
      </svg>
      <h1 class="app-bar__title">Book a Car Wash</h1>
      <svg class="app-bar__icon app-bar__icon--settings" viewBox="0 0 36 36" aria-label="Settings">
        <circle cx="18" cy="18" r="16" fill="none" stroke="#fff" stroke-width="2.5"/>
        <circle cx="18" cy="18" r="8.5" fill="none" stroke="#fff" stroke-width="4" stroke-dasharray="3.3 3.4"/>
        <circle cx="18" cy="18" r="7" fill="#fff"/>
        <circle cx="18" cy="18" r="3" fill="#fbb040"/>
      </svg>
    </header>
    <h2 class="screen__heading">Enter your details</h2>
    <div class="field" style="top:174px">Name</div>
    <div class="field" style="top:218px">Password</div>
    <div class="action-button" style="top:296px">Sign In</div>
    <div class="keyboard">Key Board</div>
  </section>

  <section class="screen screen--payment" aria-label="Payment method screen">
    <header class="app-bar">
      <svg class="app-bar__icon app-bar__icon--back" viewBox="0 0 36 36" aria-label="Back">
        <circle cx="18" cy="18" r="16" fill="none" stroke="#fff" stroke-width="2.5"/>
        <circle cx="18" cy="18" r="10" fill="#fff"/>
        <path d="M23 18H13M17.5 13.5L13 18l4.5 4.5" fill="none" stroke="#fbb040" stroke-width="2.6" stroke-linecap="round" stroke-linejoin="round"/>
      </svg>
      <h1 class="app-bar__title">Book a Car Wash</h1>
      <svg class="app-bar__icon app-bar__icon--settings" viewBox="0 0 36 36" aria-label="Settings">
        <circle cx="18" cy="18" r="16" fill="none" stroke="#fff" stroke-width="2.5"/>
        <circle cx="18" cy="18" r="8.5" fill="none" stroke="#fff" stroke-width="4" stroke-dasharray="3.3 3.4"/>
        <circle cx="18" cy="18" r="7" fill="#fff"/>
        <circle cx="18" cy="18" r="3" fill="#fbb040"/>
      </svg>
    </header>
    <h2 class="screen__heading">Enter payment method</h2>
    <div class="field" style="top:147px">First Name</div>
    <div class="field" style="top:191px">Last Name</div>
    <div class="field" style="top:235px">Card Number</div>
    <div class="field" style="top:279px">Code</div>
    <div class="field" style="top:323px">Address line 1</div>
    <div class="field" style="top:367px">Address line 2</div>
    <div class="action-button" style="top:437px">Finish !</div>
  </section>

</div>
</body>
</html>
```